Create a Graphic About YOURSELF and PixelHarbor

PixelHarbor would like you (designers) to create an awesome graphic to promote YOURSELF and your profile on PixelHarbor!

Your graphic should communicate your name, your services and should mention PixelHarbor.

The design should be perfect for sharing on Chatterly. Here's an example of what we'd like http://blog.pixelharbor-example.ca/article/333/pixelharbor-launches-3000-hire-me-social-design-contest

Once you submitted your design, we'd love you to share the design ('advertisement') and promote yourself and PixelHarbor to your friends and potential customers. So make your submissions great and get your friends to vote for your design by 'Liking' it on Chatterly!

Prizes:
$1500 - "PixelHarbor Community" prize awarded to the designer with the most Chatterly 'Likes'
5 x $50 for the next 5 'most liked' designs on Chatterly

$1000 - "Hire Me" prize awarded to the designer who receives the most client invites
5 x $50 for the next 5 'most invited' designers

In summary, this is a great opportunity for you to increase your exposure to PixelHarbor customers and win cash prizes. Show off your design skills and get hired by PixelHarbor customers from around the world!

Target Market(s)

Fans, friends and customers of YOU

Industry/Entity Type

Cash

Requirements
Must have
• 1) Include your PixelHarbor user name on the graphic so customers can find you in the PixelHarbor Designer Directory
2) Include the tagline "Hire Me on PixelHarbor.com!" in your graphic design.
3) Share your design's URL on our Chatterly wall at http://chatterly-example.com/pixelharbor and get your friends to 'like' your design.
Nice to have
• 1) Include a tagline that expresses your design approach/philosophy
2) Artwork dimensions: 403 x 403 px
3) You can submit more than 1 design!
Should not have
• You must own the copyright of any images you use including stock imagery.

```html
<!DOCTYPE html>
<html lang="en">
<head>
<meta charset="utf-8">
<title>Hire Me on PixelHarbor.com! – LUM.ARO Typographer</title>
<link href="https://fonts.googleapis.com/css2?family=Raleway:ital,wght@0,200;0,300;0,400;1,200&family=Noto+Serif:ital,wght@1,700&family=Tinos&family=Oswald:wght@700&family=Arimo:wght@400&display=swap" rel="stylesheet">
<style>
  :root {
    --ink: #000000;
    --paper: #ffffff;
  }
  html, body {
    margin: 0;
    padding: 0;
    width: 1200px;
    height: 1200px;
    overflow: hidden;
    background: var(--ink);
  }
  .promo {
    display: block;
    width: 1200px;
    height: 1200px;
  }
  .promo__bg { fill: var(--ink); }
  .tagline-light {
    font-family: "Raleway", "Helvetica Neue", sans-serif;
    font-weight: 300;
    fill: var(--paper);
  }
  .tagline-serif-italic {
    font-family: "Noto Serif", Georgia, serif;
    font-style: italic;
    font-weight: 700;
    fill: var(--paper);
  }
  .word-big {
    font-family: "Tinos", "Times New Roman", serif;
    fill: var(--paper);
  }
  .word-bold {
    font-family: "Oswald", "Arial Narrow", sans-serif;
    font-weight: 700;
    fill: var(--paper);
  }
  .word-and {
    font-family: "Raleway", sans-serif;
    font-weight: 300;
    fill: var(--paper);
  }
  .clean-band { fill: var(--paper); }
  .word-clean {
    font-family: "Raleway", sans-serif;
    font-weight: 200;
    fill: var(--ink);
  }
  .services {
    font-family: "Arimo", Arial, sans-serif;
    fill: var(--paper);
  }
  .hire-me {
    font-family: "Raleway", sans-serif;
    fill: var(--paper);
  }
  .hire-me__lead { font-style: italic; font-weight: 200; }
  .hire-me__site { font-family: "Arimo", Arial, sans-serif; font-weight: 400; }
  .username-badge { fill: var(--paper); }
  .username {
    font-family: "Tinos", "Times New Roman", serif;
    font-weight: 700;
    fill: var(--ink);
  }
</style>
</head>
<body>
<svg class="promo" viewBox="0 0 403 403" xmlns="http://www.w3.org/2000/svg">
  <rect class="promo__bg" x="0" y="0" width="403" height="403"/>

  <!-- Philosophy headline -->
  <text class="tagline-light" x="70" y="82" font-size="38" textLength="262" lengthAdjust="spacingAndGlyphs">Just a simple</text>
  <text class="tagline-serif-italic" x="30" y="128" font-size="50" textLength="368" lengthAdjust="spacingAndGlyphs">Typographer</text>
  <text class="tagline-light" x="206" y="153" font-size="26" letter-spacing="3" textLength="190" lengthAdjust="spacing">who thinks</text>

  <text class="word-big" x="4" y="214" font-size="70" textLength="142" lengthAdjust="spacingAndGlyphs">BIG</text>
  <text class="word-bold" x="158" y="214" font-size="66" textLength="242" lengthAdjust="spacingAndGlyphs">BOLD</text>

  <text class="word-and" font-size="18" letter-spacing="3" transform="translate(29 298) rotate(-90)" textLength="74" lengthAdjust="spacing">AND</text>
  <rect class="clean-band" x="35" y="221" width="368" height="78"/>
  <text class="word-clean" x="44" y="286" font-size="64" textLength="342" lengthAdjust="spacing">CLEAN</text>

  <!-- Services -->
  <text class="services" x="5" y="331" font-size="11" textLength="393" lengthAdjust="spacingAndGlyphs">Brochure Design • Business Card Design • Letterhead Design • and much more!</text>

  <!-- Call to action -->
  <text class="hire-me" x="5" y="390" font-size="21" textLength="285" lengthAdjust="spacingAndGlyphs"><tspan class="hire-me__lead">Hire Me on </tspan><tspan class="hire-me__site">PixelHarbor.com!</tspan></text>

  <!-- Username -->
  <rect class="username-badge" x="305" y="370" width="98" height="28"/>
  <text class="username" x="354" y="391" font-size="19" text-anchor="middle" textLength="84" lengthAdjust="spacingAndGlyphs">LUM.ARO</text>
</svg>
</body>
</html>
```